3 point buck deer with toolbelt

I would like to have a logo that has a 3 point buck deer as a handyman/tuff guy with a tool belt on, flexing and holding a hammer.

Target Market(s)

homeowners

Industry/Entity Type

Handyman

Contact Information for Business Card

Ridgeway Builders; Dalton R. Merrow; 4817 Larkspur Ct., Leavenworth, Wa 98734; 425.555.0147; ridgewaybuilders@mailnest.example

Font styles to use
Serif

Requirements
Must have
• a 3 point buck deer with a toolbelt
Nice to have
• hammer, broom, saw
Should not have
• the color pink

```html
<!DOCTYPE html>
<html lang="en">
<head>
<meta charset="utf-8">
<title>Ridgeway Builders – Business Card</title>
<link rel="stylesheet" href="https://fonts.googleapis.com/css2?family=Cormorant+SC:wght@500;600&family=Tinos&display=swap">
<style>
  :root {
    --page-bg: #e9e7e3;
    --card-bg: #ffffff;
    --card-shade: #f1f1f1;
    --accent: #e0502b;
    --ink: #2b2b2b;
    --ink-soft: #3d3d3d;
    --rule: #4a4a4a;
    --art-warm: #d9b77a;
    --art-red: #c9553a;
    --art-cream: #f3ead6;
  }
  * { margin: 0; padding: 0; box-sizing: border-box; }
  html, body {
    width: 1200px;
    height: 1023px;
    overflow: hidden;
    background: var(--page-bg);
  }
  .stage {
    width: 1200px;
    height: 1023px;
    display: flex;
    align-items: center;
    justify-content: center;
  }
  .card {
    position: relative;
    width: 1000px;
    height: 572px;
    background: linear-gradient(135deg, var(--card-bg) 0%, var(--card-shade) 100%);
    box-shadow: 0 18px 40px rgba(0,0,0,0.18);
    display: flex;
    align-items: center;
  }
  .card__art-zone {
    width: 420px;
    height: 100%;
    display: flex;
    align-items: center;
    justify-content: center;
  }
  .mascot-placeholder {
    width: 300px;
    height: 300px;
    border-radius: 50%;
    background: radial-gradient(circle at 45% 45%, var(--art-cream) 0%, var(--art-warm) 55%, var(--art-red) 100%);
    opacity: 0.85;
  }
  .card__divider {
    width: 2px;
    height: 412px;
    background: var(--rule);
  }
  .card__details {
    padding-left: 70px;
    display: flex;
    flex-direction: column;
  }
  .company-name {
    font-family: "Cormorant SC", "Times New Roman", serif;
    font-weight: 600;
    font-size: 46px;
    letter-spacing: 2px;
    color: var(--accent);
    margin-bottom: 60px;
  }
  .person-name {
    font-family: "Cormorant SC", "Times New Roman", serif;
    font-weight: 500;
    font-size: 36px;
    letter-spacing: 2px;
    color: var(--ink);
    margin-bottom: 48px;
  }
  .address {
    font-family: "Tinos", "Times New Roman", serif;
    font-size: 22px;
    line-height: 1.3;
    color: var(--ink-soft);
    font-style: normal;
    margin-bottom: 26px;
  }
  .contact-list { list-style: none; }
  .contact-item {
    display: flex;
    align-items: center;
    gap: 14px;
    font-family: "Tinos", "Times New Roman", serif;
    font-size: 22px;
    color: var(--ink-soft);
    margin-bottom: 10px;
  }
  .contact-icon {
    width: 26px;
    height: 26px;
    flex: none;
  }
</style>
</head>
<body>
<main class="stage">
  <article class="card">
    <div class="card__art-zone">
      <div class="mascot-placeholder" role="img" aria-label="Illustration of a handyman mascot in a round badge, holding a paint roller and a power drill, wearing a tool belt"></div>
    </div>
    <div class="card__divider"></div>
    <section class="card__details">
      <h1 class="company-name">Ridgeway Builders</h1>
      <h2 class="person-name">Dalton R. Merrow</h2>
      <address class="address">4817 Larkspur Ct.,<br>Leavenworth, Wa 98734</address>
      <ul class="contact-list">
        <li class="contact-item">
          <svg class="contact-icon" viewBox="0 0 26 26" aria-hidden="true">
            <rect width="26" height="26" rx="3" fill="var(--accent)"/>
            <path d="M8 6.5c1-.6 1.8-.3 2.3.6l1 2c.3.7.1 1.3-.5 1.7l-.8.5c.6 1.6 1.7 2.9 3.2 3.9l.6-.7c.5-.5 1.1-.6 1.7-.2l1.9 1.2c.8.5 1 1.4.3 2.3-1 1.2-2.5 1.6-4 .9-3.3-1.6-5.7-4.3-6.6-7.7-.4-1.6.1-3.1.9-4.5z" fill="#fff"/>
          </svg>
          <span>425.555.0147</span>
        </li>
        <li class="contact-item">
          <svg class="contact-icon" viewBox="0 0 26 26" aria-hidden="true">
            <rect width="26" height="26" rx="3" fill="var(--accent)"/>
            <rect x="5.5" y="8" width="15" height="10.5" rx="1" fill="none" stroke="#fff" stroke-width="1.6"/>
            <path d="M5.8 8.5l7.2 5.5 7.2-5.5" fill="none" stroke="#fff" stroke-width="1.6"/>
          </svg>
          <span>ridgewaybuilders@mailnest.example</span>
        </li>
      </ul>
    </section>
  </article>
</main>
</body>
</html>
```